Business card design needed

Chasing a very simplistic modern design with a logo incorporating "RTK".
I'm starting a plumbing business.
I do water, sanitary and drainage plumbing that will cover residential, commercial, rental, rural, excavation, new housing and all maintanence requirements.

Industry/Entity Type

Business

Contact Information for Business Card

RTK PLUMBING SERVICES
DAVID TRELOWEN - LICENSED PLUMBER
PHONE: 0481956274
E-MAIL: trelodw7@kestrelnet.com
NORTHERN SUBURBS

Requirements
Must have
• lower case email address

```html
<!DOCTYPE html>
<html lang="en">
<head>
<meta charset="utf-8">
<title>RTK Plumbing Services – Business Card</title>
<link rel="stylesheet" href="https://fonts.googleapis.com/css2?family=Exo+2:wght@300;400;700;800&family=Share+Tech+Mono&display=swap">
<style>
  :root {
    --page: #e4e6e7;
    --charcoal: #2b2d30;
    --charcoal-deep: #1d1f22;
    --silver: #d8dadc;
    --silver-light: #eef0f1;
    --ink: #1f2124;
    --ink-soft: #3a3d41;
    --aqua: #27b6e8;
    --logo: #e9ecee;
  }
  * { box-sizing: border-box; margin: 0; padding: 0; }
  html, body { width: 1200px; height: 960px; overflow: hidden; }
  body {
    background: var(--page);
    font-family: "Exo 2", sans-serif;
    position: relative;
  }
  .card {
    position: absolute;
    left: 280px;
    width: 640px;
    height: 390px;
    border-radius: 4px;
    overflow: hidden;
    box-shadow: 0 10px 30px rgba(0,0,0,.18);
  }
  .card--back { top: 70px; }
  .card--front { top: 500px; }
  .card__bg { position: absolute; inset: 0; width: 100%; height: 100%; }

  .brand { position: absolute; display: flex; align-items: center; gap: 10px; }
  .brand__mark {
    font-weight: 800; font-size: 60px; letter-spacing: 2px;
    color: var(--logo); line-height: 1;
  }
  .brand__words {
    font-weight: 800; font-size: 21px; line-height: 1;
    color: var(--logo); letter-spacing: 1px; text-transform: uppercase;
  }
  .card--back .brand { left: 40px; top: 70px; }
  .card--front .brand { right: 40px; top: 34px; }

  .services {
    position: absolute; right: 36px; top: 300px;
    font-family: "Share Tech Mono", monospace;
    font-size: 15px; color: var(--ink-soft);
    text-align: right; line-height: 1.6; letter-spacing: .5px;
  }
  .services .sep { color: var(--aqua); padding: 0 6px; }

  .person { position: absolute; left: 38px; top: 232px; }
  .person__name {
    font-weight: 800; font-size: 36px; letter-spacing: 1px;
    color: var(--ink); line-height: 1; text-transform: uppercase;
    border-bottom: 2px solid var(--ink); padding-bottom: 3px; display: inline-block;
  }
  .person__role {
    font-weight: 300; font-size: 15px; letter-spacing: 7px;
    color: var(--ink-soft); text-transform: uppercase; margin-top: 4px;
  }
  .contact { list-style: none; margin-top: 6px; font-family: "Share Tech Mono", monospace; }
  .contact li { display: flex; align-items: center; gap: 7px; font-size: 15px; color: var(--aqua); line-height: 1.45; }
  .contact svg { width: 13px; height: 13px; fill: var(--ink); }
  .area {
    margin-top: 6px;
    font-weight: 400; font-size: 15px; letter-spacing: 8px;
    color: var(--ink-soft); text-transform: uppercase;
  }
</style>
</head>
<body>

<section class="card card--back" aria-label="Business card back">
  <svg class="card__bg" viewBox="0 0 640 390" preserveAspectRatio="none" aria-hidden="true">
    <defs>
      <linearGradient id="darkBack" x1="0" y1="0" x2="1" y2="1">
        <stop offset="0" stop-color="var(--charcoal)"/>
        <stop offset="1" stop-color="var(--charcoal-deep)"/>
      </linearGradient>
      <linearGradient id="lightBack" x1="0" y1="0" x2="1" y2="1">
        <stop offset="0" stop-color="var(--silver-light)"/>
        <stop offset="1" stop-color="var(--silver)"/>
      </linearGradient>
    </defs>
    <rect width="640" height="390" fill="url(#darkBack)"/>
    <path d="M60 390 Q 200 120 640 40 L640 390 Z" fill="url(#lightBack)"/>
    <path d="M60 390 Q 200 120 640 40" fill="none" stroke="var(--aqua)" stroke-width="3"/>
  </svg>
  <div class="brand">
    <span class="brand__mark">RTK</span>
    <span class="brand__words">Plumbing<br>Services</span>
  </div>
  <p class="services">
    Plumbing<span class="sep">|</span>Residential<span class="sep">|</span>Commercial<span class="sep">|</span>Rental<br>
    Excavation<span class="sep">|</span>New Housing<span class="sep">|</span>Maintenance
  </p>
</section>

<section class="card card--front" aria-label="Business card front">
  <svg class="card__bg" viewBox="0 0 640 390" preserveAspectRatio="none" aria-hidden="true">
    <defs>
      <linearGradient id="darkFront" x1="0" y1="0" x2="1" y2="1">
        <stop offset="0" stop-color="var(--charcoal)"/>
        <stop offset="1" stop-color="var(--charcoal-deep)"/>
      </linearGradient>
      <linearGradient id="lightFront" x1="0" y1="0" x2="1" y2="1">
        <stop offset="0" stop-color="var(--silver-light)"/>
        <stop offset="1" stop-color="var(--silver)"/>
      </linearGradient>
    </defs>
    <rect width="640" height="390" fill="url(#darkFront)"/>
    <path d="M0 210 Q 230 130 640 118 L640 390 L0 390 Z" fill="url(#lightFront)"/>
    <path d="M0 210 Q 230 130 640 118" fill="none" stroke="var(--aqua)" stroke-width="3"/>
  </svg>
  <div class="brand">
    <span class="brand__mark">RTK</span>
    <span class="brand__words">Plumbing<br>Services</span>
  </div>
  <div class="person">
    <h1 class="person__name">David Trelowen</h1>
    <p class="person__role">Licensed Plumber</p>
    <ul class="contact">
      <li>
        <svg viewBox="0 0 24 24" aria-hidden="true"><path d="M6.6 10.8a15.1 15.1 0 0 0 6.6 6.6l2.2-2.2a1 1 0 0 1 1-.25 11.4 11.4 0 0 0 3.6.57 1 1 0 0 1 1 1V20a1 1 0 0 1-1 1A17 17 0 0 1 3 4a1 1 0 0 1 1-1h3.5a1 1 0 0 1 1 1c0 1.25.2 2.450.57 3.6a1 1 0 0 1-.25 1z"/></svg>
        0481-956-274
      </li>
      <li>
        <svg viewBox="0 0 24 24" aria-hidden="true"><path d="M2 5h20v14H2z M2 5l10 8 10-8"/></svg>
        trelodw7@kestrelnet.com
      </li>
    </ul>
    <p class="area">Northern Suburbs</p>
  </div>
</section>

</body>
</html>
```